International horse riding portal needs web design

We are looking for the web design for the new "Feldmoor" web portal.

Offers from the world of horses and riding should be found on this portal, eg from the categories riding schools, riding holidays, farriers, riding stables, riding stables. And all information about riding.

It is important that the different areas can be found easily and clearly. For some categories, some features should already be available in the search bar.

In addition, the design should make you want to go horse riding. The user should be emotionally picked up on the landing page.

In the lower area, some offers should be advertised, eg from the areas of riding holidays, riding training, and horse trading.

Please use the colors from the logo for the design.
C100 M50 Y10 K50 and C0 M20 Y60 K30

```html
<!DOCTYPE html>
<html lang="en">
<head>
<meta charset="utf-8">
<title>Feldmoor – Horse Riding Portal</title>
<link rel="stylesheet" href="https://fonts.googleapis.com/css2?family=Cinzel:wght@400;600;700&family=Montserrat:wght@400;500;600;700&family=Open+Sans:wght@400;600&display=swap">
<style>
:root{
  --navy:#0b3f6e;
  --gold:#b8924f;
  --gold-light:#d2b07a;
  --text:#444;
  --grey-bg:#efefef;
  --cream:#f6f2ea;
  --white:#fff;
}
*{box-sizing:border-box;margin:0;padding:0}
html,body{width:1200px;height:3434px;overflow:hidden}
body{position:relative;font-family:"Open Sans",sans-serif;color:var(--text);background:var(--white)}
.abs{position:absolute}
.serif{font-family:"Cinzel",serif}
.sans{font-family:"Montserrat",sans-serif}
.photo{position:absolute;overflow:hidden}

/* header */
.site-header{position:absolute;left:0;top:0;width:1200px;height:128px;background:var(--white)}
.brand{position:absolute;left:115px;top:4px;width:180px;height:116px;text-align:center}
.brand-mark{width:72px;height:72px;border-radius:50%;background:var(--gold);margin:0 auto}
.brand-name{font-family:"Cinzel",serif;font-weight:700;font-size:29px;color:var(--navy);margin-top:-4px;letter-spacing:1px}
.search{position:absolute;left:357px;top:10px;width:350px;height:36px;border:1px solid #aaa;border-radius:18px;font-family:"Montserrat",sans-serif;font-size:11px;color:#888;padding:11px 20px}
.search-btn{position:absolute;right:2px;top:2px;width:30px;height:30px;border-radius:50%;background:var(--gold)}
.top-links{position:absolute;top:19px;font-family:"Montserrat",sans-serif;font-size:13px;color:#333}
.login{position:absolute;left:1010px;top:11px;width:80px;height:34px;border-radius:17px;background:linear-gradient(90deg,var(--gold),var(--gold-light));color:#fff;font:600 13px "Montserrat",sans-serif;text-align:center;line-height:34px}
.main-nav{position:absolute;top:80px;font-family:"Montserrat",sans-serif;font-size:16px;color:#222;font-weight:500}
.main-nav span{position:absolute;white-space:nowrap}

/* hero */
.hero{position:absolute;left:0;top:128px;width:1200px;height:598px}
.hero-photo{position:absolute;inset:0;background:
  linear-gradient(180deg,#3f5a26 0%,#5d7a33 18%,#9c9a45 34%,#b49a4a 46%,#6a5233 58%,#8fa23a 70%,#a9b843 85%,#7d9a2e 100%)}
.hero-welcome{position:absolute;top:135px;width:1200px;text-align:center;color:#fff;font-family:"Cinzel",serif;font-size:38px;letter-spacing:2px}
.hero-title{position:absolute;top:172px;width:1200px;text-align:center;color:#fff;font-family:"Cinzel",serif;font-weight:700;font-size:86px;letter-spacing:3px}
.tabs{position:absolute;left:137px;top:404px;height:43px}
.tab{position:absolute;top:0;height:43px;background:var(--gold-light);color:var(--navy);font:600 16px "Montserrat",sans-serif;text-align:center;line-height:43px}
.tab.active{background:#fff}
.finder{position:absolute;left:137px;top:447px;width:933px;height:93px;background:#fff}
.radio{position:absolute;top:36px;font:15px "Open Sans",sans-serif;color:var(--navy);white-space:nowrap}
.radio i{display:inline-block;width:15px;height:15px;border:1.5px solid var(--navy);border-radius:50%;vertical-align:-2px;margin-right:6px;position:relative}
.radio i.on::after{content:"";position:absolute;left:3px;top:3px;width:6px;height:6px;border-radius:50%;background:var(--navy)}
.zip{position:absolute;left:604px;top:23px;width:312px;height:45px;border:1px solid #ccc;border-radius:23px;font-size:12px;color:#888;padding:14px 34px}
.find{position:absolute;right:-1px;top:-1px;width:92px;height:45px;border-radius:0 23px 23px 0;background:var(--navy);color:#fff;font:700 15px "Montserrat",sans-serif;text-align:center;line-height:45px}

/* intro */
.section-title{position:absolute;width:1200px;text-align:center;font-family:"Cinzel",serif;color:var(--navy);font-size:29px;line-height:37px;letter-spacing:1px}
.rule{position:absolute;height:2px;background:var(--gold)}
.intro-text{position:absolute;top:916px;width:445px;font-size:15.5px;line-height:24.5px;color:#444}
.cat{position:absolute;top:1077px;width:206px;height:206px;border-radius:50%;border:2px solid var(--gold);padding:6px}
.cat div{width:100%;height:100%;border-radius:50%}
.cat-label{position:absolute;top:1297px;font:700 16.5px "Montserrat",sans-serif;color:var(--gold);white-space:nowrap;text-align:center;width:206px}
.arrow{position:absolute;width:44px;height:44px;border-radius:50%;background:#f5ead8}

/* offers */
.offers{position:absolute;left:0;top:1397px;width:1200px;height:620px;background:var(--grey-bg)}
.card{position:absolute;top:133px;width:308px;height:403px;background:#fff;border:1px solid #ccc}
.card.dark{background:var(--navy);border-bottom:3px solid var(--gold)}
.card-photo{height:217px}
.card h3{margin:25px 0 0 32px;font:700 17px/20px "Montserrat",sans-serif;color:var(--navy);width:250px}
.card.dark h3{color:#fff}
.card p{margin:8px 0 0 32px;font:13px/20px "Open Sans",sans-serif;color:#777;width:250px}
.card.dark p{color:#e5e5e5}
.btn{display:block;width:135px;height:36px;border-radius:18px;background:linear-gradient(90deg,var(--gold),var(--gold-light));color:#fff;font:700 11px/36px "Montserrat",sans-serif;text-align:center}
.card .btn{margin:14px 0 0 32px}

/* training */
.training-title{position:absolute;left:123px;top:2112px;font-family:"Cinzel",serif;font-weight:600;font-size:46px;line-height:46px;color:var(--navy);letter-spacing:1px}
.training-title span{color:var(--gold)}
.training-text{position:absolute;left:128px;top:2237px;width:420px;font-size:17.5px;line-height:26.5px;color:#333}

/* horses */
.horses{position:absolute;left:0;top:2543px;width:1200px;height:520px;background:var(--cream)}
.horse{position:absolute;top:159px;width:252px;height:265px}
.horse-feature{position:absolute;left:359px;top:142px;width:252px;height:300px;background:#222;box-shadow:0 4px 12px rgba(0,0,0,.35)}

/* footer */
.site-footer{position:absolute;left:0;top:3063px;width:1200px;height:371px;background:var(--navy);color:#fff}
.foot-h{position:absolute;top:64px;font:700 15px "Cinzel",serif;letter-spacing:.5px}
.foot-h::after{content:"";position:absolute;left:0;top:28px;width:40px;height:2px;background:#fff}
.foot-list{position:absolute;font:12px "Montserrat",sans-serif;line-height:29px}
.foot-contact{position:absolute;left:580px;font:12px/20px "Montserrat",sans-serif}
.social{position:absolute;top:205px;width:24px;height:24px;border-radius:50%;border:2px solid #fff}
.copy{position:absolute;top:3406px;width:1200px;text-align:center;font:13px "Montserrat",sans-serif;color:#fff}
</style>
</head>
<body>

<header class="site-header">
  <div class="brand">
    <div class="brand-mark"></div>
    <div class="brand-name">FELDMOOR</div>
  </div>
  <div class="search">Search &gt; Feature
    <div class="search-btn"><svg width="30" height="30" viewBox="0 0 30 30"><circle cx="14" cy="14" r="6" fill="none" stroke="#fff" stroke-width="2.5"/><line x1="18.5" y1="18.5" x2="22" y2="22" stroke="#fff" stroke-width="2.5"/></svg></div>
  </div>
  <span class="top-links" style="left:777px">News</span>
  <span class="top-links" style="left:841px">Resources</span>
  <span class="top-links" style="left:935px">My List</span>
  <div class="login">Login</div>
  <nav class="main-nav">
    <span style="left:341px">About Us ⌄</span>
    <span style="left:462px">Riding School ⌄</span>
    <span style="left:608px">Riding Holidays ⌄</span>
    <span style="left:768px">Farries ⌄</span>
    <span style="left:865px">Riding Stables ⌄</span>
    <span style="left:1017px">Contact</span>
  </nav>
</header>

<section class="hero">
  <div class="hero-photo" role="img" aria-label="Three horses grazing in a sunlit green paddock behind a dark wooden fence, hay bales and trees in the distance"></div>
  <div class="hero-welcome">—WELCOME TO—</div>
  <div class="hero-title">FELDMOOR</div>
  <div class="tabs">
    <div class="tab active" style="left:0;width:166px">Riding School</div>
    <div class="tab" style="left:174px;width:170px">Riding Holidays</div>
    <div class="tab" style="left:348px;width:123px">Farries</div>
    <div class="tab" style="left:475px;width:163px">Riding Stables</div>
  </div>
  <div class="finder">
    <span class="radio" style="left:32px"><i class="on"></i>Feature First</span>
    <span class="radio" style="left:160px"><i></i>Feature Second</span>
    <span class="radio" style="left:314px"><i></i>Feature Third</span>
    <span class="radio" style="left:455px"><i></i>Feature Fourth</span>
    <div class="zip">Zip Code/ City
      <svg class="abs" style="left:14px;top:13px" width="12" height="16" viewBox="0 0 12 16"><path d="M6 1a5 5 0 0 1 5 5c0 4-5 9-5 9S1 10 1 6a5 5 0 0 1 5-5z" fill="none" stroke="#888" stroke-width="1.5"/><circle cx="6" cy="6" r="1.8" fill="#888"/></svg>
      <div class="find">FIND</div>
    </div>
  </div>
</section>

<h2 class="section-title" style="top:794px">IHIC TECTIO BLAB INCIENIS AUT HILIQUO QUISQUI<br>AEPRECTUR? URESEQUOD QUI DITIS</h2>
<div class="rule" style="left:553px;top:878px;width:94px"></div>
<div class="rule" style="left:578px;top:884px;width:44px"></div>
<p class="intro-text" style="left:121px">Lorem ipsum dolor sit amet, consectetur adipiscing elit, sed do eiusmod tempor incididunt ut labore et dolore magna aliqua. Ut enim ad minim.Lorem ipsum dolor sit amet.Lorem ipsum dolor sit amet, consectetur adipiscing.</p>
<p class="intro-text" style="left:618px">Lorem ipsum dolor sit amet, consectetur adipiscing elit, sed do eiusmod tempor incididunt ut labore et dolore magna aliqua. Ut enim ad minim.Lorem ipsum dolor sit amet.Lorem ipsum dolor sit amet, consectetur adipiscing.</p>

<div class="arrow" style="left:18px;top:1154px"><svg width="44" height="44"><path d="M25 14l-8 8 8 8" fill="none" stroke="#0b3f6e" stroke-width="3"/></svg></div>
<div class="arrow" style="left:1145px;top:1154px"><svg width="44" height="44"><path d="M19 14l8 8-8 8" fill="none" stroke="#0b3f6e" stroke-width="3"/></svg></div>
<div class="cat" style="left:73px"><div role="img" aria-label="Smiling rider leaning forward to hug her grey horse" style="background:linear-gradient(160deg,#d9d6cf 0%,#8d8a84 45%,#5b5853 100%)"></div></div>
<div class="cat" style="left:289px"><div role="img" aria-label="Group of riders heading out on a holiday trail in evening light" style="background:linear-gradient(160deg,#f2c69a 0%,#d8875a 40%,#6b3b2a 100%)"></div></div>
<div class="cat" style="left:504px"><div role="img" aria-label="Rider on a chestnut horse in a sunny outdoor arena" style="background:linear-gradient(180deg,#3f6a2c 0%,#7a8f3e 35%,#b9824d 65%,#c9a77e 100%)"></div></div>
<div class="cat" style="left:719px"><div role="img" aria-label="Horses looking out of their stable boxes along an aisle" style="background:linear-gradient(90deg,#3d3a35 0%,#7d7a72 40%,#d8d4cb 55%,#5a4a3a 100%)"></div></div>
<div class="cat" style="left:933px"><div role="img" aria-label="Close view of a rider on a brown and white horse" style="background:linear-gradient(160deg,#e6dccb 0%,#a47a52 45%,#4a2f1e 100%)"></div></div>
<div class="cat-label" style="left:60px">RIDING SCHOOLS</div>
<div class="cat-label" style="left:281px">RIDING HOLIDAYS</div>
<div class="cat-label" style="left:506px">RIDING FARRIERS</div>
<div class="cat-label" style="left:725px">RIDING STABLES</div>
<div class="cat-label" style="left:939px">ABOUT RIDING</div>

<section class="offers">
  <h2 class="section-title" style="top:48px;font-size:33px">IHIC TECTIO BLAB <span style="color:var(--gold)">INCIENIS AUT</span></h2>
  <div class="rule" style="left:553px;top:98px;width:94px"></div>
  <div class="rule" style="left:578px;top:104px;width:44px"></div>
  <div class="arrow" style="left:50px;top:306px"><svg width="44" height="44"><path d="M25 14l-8 8 8 8" fill="none" stroke="#0b3f6e" stroke-width="3"/></svg></div>
  <div class="arrow" style="left:1105px;top:306px"><svg width="44" height="44"><path d="M19 14l8 8-8 8" fill="none" stroke="#0b3f6e" stroke-width="3"/></svg></div>
  <article class="card dark" style="left:124px">
    <div class="card-photo" role="img" aria-label="Instructor teaching a young rider on a chestnut pony in an outdoor arena" style="background:linear-gradient(180deg,#8fb06a 0%,#5f7f3e 40%,#b08a5e 62%,#d9cbb6 100%)"></div>
    <h3>Sed ut perspiciatis unde omnis iste natus</h3>
    <p>Lorem ipsum dolor sit amet, consect-etur adipiscing elit, sed eiusmod</p>
    <span class="btn">LEARN MORE ›</span>
  </article>
  <article class="card" style="left:449px">
    <div class="card-photo" role="img" aria-label="Rider cantering a bay horse through bright autumn woods" style="background:linear-gradient(180deg,#e9e3d6 0%,#cbb89a 40%,#9a6538 70%,#e2d8c6 100%)"></div>
    <h3>Sed ut perspiciatis unde omnis iste natus</h3>
    <p>Lorem ipsum dolor sit amet, consect-etur adipiscing elit, sed eiusmod</p>
    <span class="btn">LEARN MORE ›</span>
  </article>
  <article class="card" style="left:773px">
    <div class="card-photo" role="img" aria-label="Show jumper and horse clearing a fence at a competition with flags behind" style="background:linear-gradient(180deg,#a9cbe6 0%,#c8d8e4 35%,#b98a5a 60%,#6b4630 85%,#c23a3a 100%)"></div>
    <h3>Sed ut perspiciatis unde omnis iste natus</h3>
    <p>Lorem ipsum dolor sit amet, consect-etur adipiscing elit, sed eiusmod</p>
    <span class="btn">LEARN MORE ›</span>
  </article>
</section>

<h2 class="training-title">Horse Riding<br><span>Training</span></h2>
<div class="rule" style="left:123px;top:2212px;width:62px"></div>
<div class="rule" style="left:138px;top:2218px;width:32px"></div>
<p class="training-text">Lorem ipsum dolor sit amet, consectetur adipiscing elit, sed do eiusmod tempor incididunt ut labore et dolore magna aliqua. Ut enim ad minim veniam, quis nostrud exercitation ullamco laboris nisi ut al-iquip ex ea commodo consequat.</p>
<span class="btn abs" style="left:123px;top:2395px;width:160px;height:42px;line-height:42px;border-radius:21px;font-size:13px">LEARN MORE ›</span>
<svg class="abs" style="left:588px;top:2087px" width="500" height="370"><path d="M10 368 H495 V60 A70 70 0 0 0 425 0" fill="none" stroke="#b8924f" stroke-width="3"/></svg>
<div class="photo" role="img" aria-label="Happy young woman with long hair hugging a chestnut horse with a white blaze by a sunny paddock" style="left:588px;top:2087px;width:488px;height:358px;border-radius:0 80px 0 80px;background:linear-gradient(100deg,#e3cfb4 0%,#b97a45 22%,#f1e6d8 45%,#6b3a34 70%,#e9ddd0 100%)"></div>

<section class="horses">
  <h2 class="section-title" style="top:50px;font-size:37px"><span style="color:var(--gold)">OUR</span> HORSES</h2>
  <div class="rule" style="left:553px;top:100px;width:94px"></div>
  <div class="horse photo" style="left:107px;background:linear-gradient(120deg,#b9bd6a 0%,#c88a4a 35%,#a0481e 65%,#5e6f2a 100%)" role="img" aria-label="Chestnut horse with a white blaze and flowing blond mane"></div>
  <div class="horse photo" style="left:611px;background:linear-gradient(180deg,#8c9c8a 0%,#4d5a4a 30%,#1f1c1a 55%,#c43a22 85%,#7a2a18 100%)" role="img" aria-label="Black horse standing in a field of red poppies"></div>
  <div class="horse photo" style="left:864px;background:linear-gradient(180deg,#d7cf8a 0%,#b8844a 35%,#a35a2a 60%,#9fb050 100%)" role="img" aria-label="Bay horse standing alert in a summer meadow"></div>
  <div class="horse-feature">
    <div role="img" aria-label="Bay horse with a white blaze wearing a halter" style="width:100%;height:236px;background:linear-gradient(150deg,#2a2a2a 0%,#4a2a1c 45%,#8a4020 80%,#2a2a2a 100%)"></div>
    <div class="abs sans" style="left:16px;top:257px;font-size:19px;font-weight:700;color:#fff">Horse Name</div>
    <div class="abs sans" style="left:155px;top:250px;font-size:9.5px;line-height:17px;color:#fff"><b>Birth Year:</b> 2018<br><b>Gender:</b> Gelding</div>
  </div>
</section>

<footer class="site-footer">
  <div class="abs" style="left:115px;top:82px;width:200px;text-align:center">
    <div style="width:90px;height:90px;border-radius:50%;background:#fff;margin:0 auto"></div>
    <div class="serif" style="font-weight:700;font-size:31px;color:#fff;margin-top:-6px">FELDMOOR</div>
  </div>
  <div class="foot-h" style="left:358px">NAVIGATION</div>
  <div class="foot-list" style="left:358px;top:109px">About Us<br>&nbsp;Riding School<br>Riding Holidays<br>Farries<br>Riding Stables</div>
  <div class="foot-h" style="left:545px">CONTACT US</div>
  <svg class="abs" style="left:549px;top:116px" width="16" height="20" viewBox="0 0 16 20"><path d="M8 1a7 7 0 0 1 7 7c0 5-7 11-7 11S1 13 1 8a7 7 0 0 1 7-7z" fill="#fff"/><circle cx="8" cy="8" r="2.5" fill="#0b3f6e"/></svg>
  <div class="foot-contact" style="top:118px">48 Meadowbrook Lane P.O. Box 212<br>Greenfield, Ontario&nbsp; K0L 2H0</div>
  <svg class="abs" style="left:548px;top:169px" width="20" height="20" viewBox="0 0 20 20"><path d="M4 1l4 4-2 3c1 3 3 5 6 6l3-2 4 4-3 3C9 19 1 11 1 4z" fill="#fff"/></svg>
  <div class="foot-contact" style="top:169px">Tel: (555) 014-2870</div>
  <svg class="abs" style="left:549px;top:204px" width="20" height="14" viewBox="0 0 20 14"><rect x="1" y="1" width="18" height="12" fill="none" stroke="#fff" stroke-width="1.8"/><path d="M1 1l9 7 9-7" fill="none" stroke="#fff" stroke-width="1.8"/></svg>
  <div class="foot-contact" style="top:201px">Email: info@feldmoor.com</div>
  <div class="foot-h" style="left:840px">FOLLOW US</div>
  <div class="abs" style="left:840px;top:110px;width:210px;height:34px;background:#fff;font:10px/34px 'Montserrat',sans-serif;color:#888;padding-left:14px">Your Email address</div>
  <div class="abs sans" style="left:905px;top:166px;font-size:11px;font-weight:700">SUBSCRIBE</div>
  <div class="social" aria-label="Social link" style="left:842px"></div>
  <div class="social" aria-label="Social link" style="left:881px"></div>
  <div class="social" aria-label="Social link" style="left:918px"></div>
  <div class="abs" style="left:0;top:327px;width:1200px;height:1px;background:rgba(255,255,255,.2)"></div>
</footer>
<div class="copy">Copyright © 2022 Feldmoor All Right Reserved</div>

</body>
</html>
```